Hot Dog Anhänger
Sofort das richtige Design getroffen. Vielen Dank!
Zielgruppe
Wir sind im Bereich der Reisegastronomie tätig und stehen mit diversen Geschäften auf Stadt- und Straßenfesten, Weihnachtsmärkten und ähnlichen Veranstaltungen. Dieser Anhänger soll speziell für den Verkauf von Hot Dogs sein.
Aufgabenstellung
Der Anhänger soll optisch ordentlich etwas her machen, weshalb eine Vollverklebung/Folierung von allen vier Seiten angedacht ist. Der Anhänger selbst hat keine weitere Außenbeleuchtung, daher muss das Design sehr ansprechend sein.
Es soll ein reiner Hot Dog Anhänger werden. Sehr schön fände ich ein Retro-Design, jedoch bitte nichts mit Amerika-Fahnen, Wolkenbrunnen, Pfad 19 oder ähnliches.
Unter der Verkaufsklappe sollte der Schriftzug "Hot Dogs" zu lesen sein, so dass man auch bei geöffneter Klappe sehen kann, was es dort zu essen gibt.
Hier habe ich mal einen Anhänger gefunden, der ein Stück weit in die angedachte Richtung geht, wenngleich das dortige Design mich jetzt auch nicht vom Stuhl gehauen hat:
http://www.rollmarkt-beispiel.example/angebote/Anh%C3%A4nger-Kastenwagen-2-00m-Brenno-Hot-Dog-Kiosk-Verkaufsanh%C3%A4nger/48302716/1
Das Design bzw. die späteren Druckdateien sollten in einer sehr hohen Auslösung verfügbar sein, so dass die Klebefolien fotorealistisch ausgedruckt werden könnten. Es reicht aus, wenn zwei Seiten (1x längste, 1x kürzeste) des Anhängers gestaltet werden. Dieses Design würde ich dann auch für die anderen beiden Seiten nutzen.

```html
<!DOCTYPE html>
<html lang="de">
<head>
<meta charset="utf-8">
<title>Hot Dog Anhänger – Seitenansichten</title>
<link rel="stylesheet" href="https://fonts.googleapis.com/css2?family=Chango&family=Kaushan+Script&display=swap">
<style>
  :root {
    --awning-red: #c4161c;
    --awning-yellow: #f7b334;
    --sky-light: #eef3f4;
    --sky-mid: #a9c2c8;
    --sky-dark: #7a9ea7;
    --ground: #e6c9a5;
    --ground-edge: #f1dcc2;
    --badge: #5e8b96;
    --title-red: #c8202a;
    --title-outline: #4a2513;
    --title-highlight: #f4b53a;
    --ink: #2e1b10;
    --bun-light: #f4b67a;
    --bun-dark: #b5532a;
    --page: #ffffff;
    --panel-edge: #6d6d6d;
  }
  html, body {
    margin: 0;
    padding: 0;
    width: 1095px;
    height: 1200px;
    overflow: hidden;
    background: var(--page);
  }
  .sheet {
    position: relative;
    width: 1095px;
    height: 1200px;
  }
  .side-panel {
    position: absolute;
    top: 332px;
    display: block;
  }
  .side-panel--long { left: 0; width: 581px; height: 536px; }
  .side-panel--short { left: 617px; width: 478px; height: 534px; outline: 1px solid var(--panel-edge); }
  .title {
    font-family: "Chango", "Cooper Black", serif;
    fill: var(--title-red);
    stroke: var(--title-outline);
    stroke-width: 10px;
    paint-order: stroke;
  }
  .badge-text, .tagline {
    font-family: "Kaushan Script", cursive;
  }
  .badge-text { fill: #ffffff; }
  .tagline { fill: var(--ink); }
</style>
</head>
<body>
<main class="sheet">

  <svg class="side-panel side-panel--long" viewBox="0 0 977 900" aria-label="Längsseite des Anhängers">
    <defs>
      <radialGradient id="sky-long" cx="0.5" cy="0.6" r="0.75">
        <stop offset="0" stop-color="var(--sky-light)"/>
        <stop offset="0.45" stop-color="var(--sky-mid)"/>
        <stop offset="1" stop-color="var(--sky-dark)"/>
      </radialGradient>
      <linearGradient id="hotdog-long" x1="0" y1="0" x2="1" y2="1">
        <stop offset="0" stop-color="var(--bun-dark)"/>
        <stop offset="0.5" stop-color="var(--bun-light)"/>
        <stop offset="1" stop-color="#e08a4a"/>
      </linearGradient>
      <polygon id="badge-shape" points="1,0 .831,.223 .866,.5 .608,.608 .5,.866 .223,.831 0,1 -.223,.831 -.5,.866 -.608,.608 -.866,.5 -.831,.223 -1,0 -.831,-.223 -.866,-.5 -.608,-.608 -.5,-.866 -.223,-.831 0,-1 .223,-.831 .5,-.866 .608,-.608 .866,-.5 .831,-.223"/>
    </defs>
    <rect class="sky" width="977" height="900" fill="url(#sky-long)"/>

    <g class="awning">
      <path d="M0 0H244V20Q244 45 219 45H25Q0 45 0 20Z" fill="var(--awning-red)"/>
      <path d="M244 0H488V20Q488 45 463 45H269Q244 45 244 20Z" fill="var(--awning-yellow)"/>
      <path d="M488 0H732V20Q732 45 707 45H513Q488 45 488 20Z" fill="var(--awning-red)"/>
      <path d="M732 0H977V20Q977 45 952 45H757Q732 45 732 20Z" fill="var(--awning-yellow)"/>
    </g>

    <path class="ground" d="M0 830Q480 715 977 735V900H0Z" fill="var(--ground)"/>

    <ellipse class="hotdog-illustration" role="img" aria-label="Illustration: Hot Dog mit Senf und Ketchup" cx="460" cy="360" rx="275" ry="105" transform="rotate(-25 460 360)" fill="url(#hotdog-long)"/>

    <g class="badge" transform="translate(680 465) rotate(-8)">
      <use href="#badge-shape" transform="scale(122)" fill="var(--badge)" stroke="var(--badge)" stroke-width="0.08" stroke-linejoin="round"/>
      <text class="badge-text" x="0" y="-18" font-size="54" text-anchor="middle">fresh</text>
      <text class="badge-text" x="5" y="50" font-size="54" text-anchor="middle">&amp; hot</text>
    </g>

    <ellipse class="snack-illustration" role="img" aria-label="Kleine Illustration: Hot Dog" cx="110" cy="805" rx="85" ry="40" transform="rotate(25 110 805)" fill="url(#hotdog-long)"/>

    <text class="title" x="530" y="825" font-size="118" text-anchor="middle" transform="rotate(-7 530 790)">Hot Dogs</text>
    <text class="tagline" x="730" y="858" font-size="48" transform="rotate(-4 730 858)">Enjoy it!</text>
  </svg>

  <svg class="side-panel side-panel--short" viewBox="0 0 803 898" aria-label="Stirnseite des Anhängers">
    <defs>
      <radialGradient id="sky-short" cx="0.45" cy="0.6" r="0.75">
        <stop offset="0" stop-color="var(--sky-light)"/>
        <stop offset="0.45" stop-color="var(--sky-mid)"/>
        <stop offset="1" stop-color="var(--sky-dark)"/>
      </radialGradient>
      <linearGradient id="hotdog-short" x1="1" y1="0" x2="0" y2="1">
        <stop offset="0" stop-color="var(--bun-dark)"/>
        <stop offset="0.5" stop-color="var(--bun-light)"/>
        <stop offset="1" stop-color="#e08a4a"/>
      </linearGradient>
    </defs>
    <rect class="sky" width="803" height="898" fill="url(#sky-short)"/>

    <g class="awning">
      <path d="M0 0H262V18Q262 42 238 42H24Q0 42 0 18Z" fill="var(--awning-red)"/>
      <path d="M262 0H528V18Q528 42 504 42H286Q262 42 262 18Z" fill="var(--awning-yellow)"/>
      <path d="M528 0H803V18Q803 42 779 42H552Q528 42 528 18Z" fill="var(--awning-red)"/>
    </g>

    <path class="ground" d="M0 735Q420 735 803 825V898H0Z" fill="var(--ground)"/>

    <ellipse class="hotdog-illustration" role="img" aria-label="Illustration: Hot Dog mit Senf und Ketchup" cx="490" cy="370" rx="225" ry="90" transform="rotate(25 490 370)" fill="url(#hotdog-short)"/>

    <g class="badge" transform="translate(288 465) rotate(-8)">
      <use href="#badge-shape" transform="scale(100)" fill="var(--badge)" stroke="var(--badge)" stroke-width="0.08" stroke-linejoin="round"/>
      <text class="badge-text" x="0" y="-14" font-size="46" text-anchor="middle">fresh</text>
      <text class="badge-text" x="4" y="44" font-size="46" text-anchor="middle">&amp; hot</text>
    </g>

    <ellipse class="snack-illustration" role="img" aria-label="Kleine Illustration: Hot Dog" cx="720" cy="812" rx="60" ry="28" transform="rotate(-28 720 812)" fill="url(#hotdog-short)"/>

    <text class="title" x="400" y="790" font-size="92" text-anchor="middle" transform="rotate(6 400 760)">Hot Dogs</text>
    <text class="tagline" x="55" y="855" font-size="44" transform="rotate(-4 55 855)">Enjoy it!</text>
  </svg>

</main>
</body>
</html>
```